Web Design Project for Wren Nectar

We are a Honey Packing Company called Wren Nectar.
We need a new website.
We are open to many ideas.
We want to have headings like: Home/Products/About Us/Contact Us
We want an easy and uncomplicated website.
We need our logo attached to the center top or left top of the webpage.
We want to have a number of our products on the first page that increase in size once the cursor is placed on them.
We want to be able to add photos and products in the future as we expand.
Updates
Target Market(s)
Public
Food Distributors
Importers/Exporters
Industry/Entity Type
It Company
Look and feel
Each slider illustrates characteristics of the customer's brand and the style your logo design should communicate.

```html
<!DOCTYPE html>
<html lang="en">
<head>
<meta charset="utf-8">
<title>Wren Nectar – Home</title>
<link href="https://fonts.googleapis.com/css2?family=Tinos:wght@400;700&display=swap" rel="stylesheet">
<style>
  :root {
    --page-bg: #f2ef9c;
    --header-cream: #fbf8e6;
    --panel-white: #ffffff;
    --ink: #2b2520;
    --brown: #5a3218;
    --rule: #6b4a33;
    --link-brown: #8a5a1e;
    --honey-light: #f2b640;
    --honey-mid: #d97f12;
    --honey-dark: #9a4a08;
    --lid-orange: #f2a21a;
  }
  * { box-sizing: border-box; margin: 0; padding: 0; }
  html, body {
    width: 1084px; height: 1200px; overflow: hidden;
    background: var(--page-bg);
    font-family: "Tinos", "Times New Roman", serif;
    color: var(--ink);
  }
  .site { position: relative; width: 1084px; height: 1200px; }

  .top-bar {
    position: absolute; left: 36px; top: 102px; width: 1010px; height: 58px;
    background: var(--header-cream);
    border-radius: 14px 14px 0 0;
    box-shadow: 0 2px 4px rgba(0,0,0,0.12);
  }
  .tagline {
    position: absolute; top: 17px; font-size: 18px; letter-spacing: 0.3px;
    text-transform: uppercase; transform: translateX(-50%); white-space: nowrap;
  }
  .tagline--left { left: 204px; }
  .tagline--right { left: 813px; }

  .brand-badge {
    position: absolute; left: 446px; top: 31px; width: 192px; height: 192px;
    border-radius: 50%; background: var(--panel-white);
    border: 2px solid var(--brown);
    box-shadow: 0 0 0 3px #fff, 0 2px 6px rgba(0,0,0,0.2);
    display: flex; align-items: center; justify-content: center; z-index: 3;
  }
  .brand-name {
    font-size: 27px; color: var(--brown); text-align: center; line-height: 1.15;
  }

  .panel {
    position: absolute; left: 47px; top: 158px; width: 988px; height: 1042px;
    background: var(--panel-white);
  }
  .hero {
    width: 988px; height: 516px;
    background: radial-gradient(ellipse at 45% 45%, var(--honey-light) 0%, var(--honey-mid) 45%, var(--honey-dark) 80%, #f7f3ee 100%);
  }

  .main-nav {
    position: absolute; left: 326px; top: 522px; width: 355px; height: 36px;
    border-bottom: 1px solid var(--rule);
    display: flex; justify-content: center; gap: 21px;
  }
  .main-nav a {
    font-size: 16.5px; color: var(--ink); text-decoration: none; letter-spacing: 0.6px;
    padding-top: 8px; height: 36px;
  }
  .main-nav a.is-current { font-weight: 700; color: var(--brown); border-bottom: 3px solid var(--brown); }

  .intro { position: absolute; left: 21px; top: 570px; width: 480px; }
  .intro h1 { font-weight: 400; font-size: 25px; letter-spacing: 0.5px; margin-bottom: 18px; }
  .intro p { font-size: 16.6px; line-height: 24px; }

  .featured {
    position: absolute; left: 657px; top: 636px; width: 222px; text-align: center;
  }
  .product-shot {
    width: 222px; height: 199px; border-radius: 10px 10px 16px 16px;
    background: linear-gradient(180deg, var(--lid-orange) 0%, var(--lid-orange) 14%, var(--honey-mid) 16%, var(--honey-dark) 100%);
    box-shadow: 2px 3px 6px rgba(0,0,0,0.3);
  }
  .featured figcaption { font-size: 15px; margin-top: 14px; }

  .footer {
    position: absolute; left: 21px; top: 1002px; width: 946px;
    border-top: 1px solid var(--rule); padding-top: 10px;
    display: flex; justify-content: space-between; font-size: 12.2px;
  }
  .footer .sep { margin: 0 9px; }
  .footer .address { color: var(--link-brown); }
</style>
</head>
<body>
<div class="site">
  <header class="top-bar">
    <span class="tagline tagline--left">The Purest Honey</span>
    <span class="tagline tagline--right">100% Australian</span>
  </header>
  <div class="brand-badge"><span class="brand-name">Wren<br>Nectar</span></div>

  <main class="panel">
    <div class="hero" role="img" aria-label="Close-up of a wooden honey dipper resting in a glass jar of golden honey"></div>

    <nav class="main-nav">
      <a href="#" class="is-current">Home</a>
      <a href="#">Products</a>
      <a href="#">About Us</a>
      <a href="#">Contact Us</a>
    </nav>

    <section class="intro">
      <h1>Welcome to Wren Nectar</h1>
      <p>Interested in top quality pure 100% Australian honey? Wren Nectar is a business established to provide high quality 100% natural and contaminant free pure honey. We are able to package honey to your requirements. Private Labels are possible. Our 100% natural honey is produced in the Adelaide hills which is famous for its unique and pleasant flavor. Wren Nectar is thick and very slow to crystallize. The most popular varieties of honey we supply is loosen, eucalyptus and orange. We currently supply packaged honey in various attractive containers and bulk honey to the market. Please look around our website as well as feel free to contact us by phone or email to discuss your honey requirements. For your convenience there is a contact form link at the top of each page.</p>
    </section>

    <figure class="featured">
      <div class="product-shot" role="img" aria-label="Tub of Wren Nectar honey with an orange lid and printed label"></div>
      <figcaption>Some description</figcaption>
    </figure>

    <footer class="footer">
      <span>© 2012 Wren Nectar<span class="sep">•</span><span class="address">24 Larkspur Ct Elmridge, Adelaide, SA, Australia 5990</span></span>
      <span>Fax: +61-08-81234567<span class="sep">•</span>Telephone: +61-08-81234567<span class="sep">•</span>E-mail: hello@wrennectar.example</span>
    </footer>
  </main>
</div>
</body>
</html>
```